Car finance company business card

Create a nice business card for our car financing company , Visit our website www.brookmilefinance.com for the phone number and idea of the company look. Please do not be afraid to be creative. Name on card Is Marc-Olivier Dussault and phone number is on our website adress of business is
27816 Boulevard Des-Ormeaux,
Mirabel, QC H4R 2B6

```html
<!DOCTYPE html>
<html lang="en">
<head>
<meta charset="utf-8">
<title>Brookmile Finance – Business Card</title>
<link rel="stylesheet" href="https://fonts.googleapis.com/css2?family=Oswald:wght@500&family=Work+Sans:wght@400;600;700&display=swap">
<style>
  :root {
    --stage: #141414;
    --card: #232323;
    --card-edge: #2c2c2c;
    --ink: #f2f2f2;
    --accent: #f07a25;
    --accent-deep: #c9561a;
    --mascot-blue: #3a4a9a;
  }
  * { box-sizing: border-box; margin: 0; padding: 0; }
  html, body {
    width: 1200px; height: 900px; overflow: hidden;
    background: var(--stage);
    font-family: "Work Sans", sans-serif;
    color: var(--ink);
  }
  .stage {
    width: 1200px; height: 900px;
    display: flex; flex-direction: column; align-items: center; justify-content: center;
    gap: 40px;
  }
  .card {
    position: relative;
    width: 620px; height: 354px;
    background: linear-gradient(135deg, var(--card-edge), var(--card) 60%);
    border-radius: 3px;
    box-shadow: 0 10px 30px rgba(0,0,0,.5);
  }
  /* Front */
  .brand {
    position: absolute; left: 0; right: 0; top: 105px;
    display: flex; align-items: center; justify-content: center; gap: 22px;
  }
  .brand-name {
    font-weight: 700; font-size: 40px; line-height: 1.05;
    letter-spacing: 1px; text-transform: uppercase; color: var(--ink);
  }
  .mascot {
    width: 96px; height: 118px; border-radius: 10px;
    background: linear-gradient(160deg, var(--accent), var(--accent-deep) 55%, var(--mascot-blue));
  }
  .front-web {
    position: absolute; left: 0; right: 0; bottom: 44px;
    text-align: center; font-size: 15px; letter-spacing: .5px;
  }
  .accent { color: var(--accent); }
  /* Back */
  .identity {
    position: absolute; left: 52px; top: 128px; width: 258px; text-align: right;
  }
  .person-name {
    font-family: "Oswald", sans-serif; font-weight: 500;
    font-size: 29px; letter-spacing: 1px; text-transform: uppercase;
    color: var(--accent); line-height: 1.1;
  }
  .person-role { font-size: 15px; margin-top: 4px; }
  .divider {
    position: absolute; left: 330px; top: 130px;
    width: 1px; height: 66px; background: var(--ink);
  }
  .contacts {
    position: absolute; left: 350px; top: 124px;
    list-style: none; font-size: 15px; line-height: 26px;
  }
  .contacts li { display: flex; align-items: center; gap: 9px; }
  .contacts svg { width: 11px; height: 11px; flex: none; }
  .address {
    position: absolute; left: 0; right: 0; bottom: 42px;
    text-align: center; font-size: 15px; letter-spacing: .4px;
  }
</style>
</head>
<body>
<main class="stage">
  <section class="card card-front">
    <div class="brand">
      <span class="brand-name">Brookmile<br>Finance</span>
      <div class="mascot" role="img" aria-label="Company mascot illustration area"></div>
    </div>
    <p class="front-web">www.<span class="accent">brookmilefinance</span>.com</p>
  </section>

  <section class="card card-back">
    <div class="identity">
      <h1 class="person-name">Marc-Olivier Dussault</h1>
      <p class="person-role">Director</p>
    </div>
    <span class="divider"></span>
    <ul class="contacts">
      <li>
        <svg viewBox="0 0 12 12"><path d="M3 1 L5 3.5 L4 5 Q5.5 7 7 8 L8.5 7 L11 9 L10 11 Q5 11 1 4 Z" fill="var(--accent)"/></svg>
        (514) 555-0187
      </li>
      <li>
        <svg viewBox="0 0 12 12"><rect x="1" y="2.5" width="10" height="7" fill="none" stroke="var(--accent)" stroke-width="1.2"/><path d="M1 2.5 L6 6.5 L11 2.5" fill="none" stroke="var(--accent)" stroke-width="1.2"/></svg>
        info@brookmilefinance.com
      </li>
      <li>
        <svg viewBox="0 0 12 12"><circle cx="6" cy="6" r="5" fill="none" stroke="var(--accent)" stroke-width="1.1"/><ellipse cx="6" cy="6" rx="2.2" ry="5" fill="none" stroke="var(--accent)" stroke-width="1"/><path d="M1 6 H11" stroke="var(--accent)" stroke-width="1"/></svg>
        www.<span class="accent">brookmilefinance</span>.com
      </li>
    </ul>
    <p class="address">27816 Boulevard Des-Ormeaux, Mirabel, QC H4R 2B6</p>
  </section>
</main>
</body>
</html>
```